Create a Eye Catching Web Design

We need an informative web design that needs to be eye catching and unique. All of the information needs to be on that page - We have a shopfront setup in the next 2 weeks so the website needs to be ready asap. We are selling mainly rehabilitation aids and mobility products.

The website is main purpose is to inform customers about our range of products, address and phone number. This is an interim website until we get an ecommerce website setup. We are not looking for an ecommerce website, just simple, eye-catching and informative. clean, crisp and modern -target age 45-75 yo (men and women)

I have included our logo and brochure designed with our range of product categories.

The website needs to be designed, coded and setup completely as a finished product.

As soon as the website design is chosen, the chosen designer would need to get the website up and running. If the website design is chosen and great, we could use the same designer for the ecommerce build as well.

www.tolvenacare.com
www.tolvenacare.com.au

Reason: I haven't received as many designs but variations from the same designers.

Target Market(s)

45-75

Industry/Entity Type

Health And Wellness

Coding

Coded - Design and coding required

Number of Pages Required

2 page

Font styles to use
Sans Serif

Requirements
Nice to have
• clean design, modern feel - not cluttered - something unique. for the market age

```html
<!DOCTYPE html>
<html lang="en">
<head>
<meta charset="utf-8">
<title>Tolvena Mobility</title>
<link href="https://fonts.googleapis.com/css2?family=Fira+Sans:ital,wght@0,400;0,500;0,600;1,500&display=swap" rel="stylesheet">
<style>
:root{
  --red:#ed1c24;
  --ink:#4a4a4a;
  --muted:#6b6b6b;
  --band:#f4f3ef;
  --footer:#737373;
  --footer-dark:#484848;
  --white:#ffffff;
}
*{margin:0;padding:0;box-sizing:border-box}
html,body{width:1096px;height:1200px;overflow:hidden;background:var(--white)}
body{position:relative;font-family:"Fira Sans",sans-serif;color:var(--ink)}
.abs{position:absolute}
.intro-art{left:110px;top:-48px;width:156px;height:156px;border-radius:50%;background:var(--red)}
.intro-text{left:349px;top:-5px;width:560px;font-size:12px;line-height:24px;letter-spacing:.3px;color:var(--ink)}
.intro-text p+p{margin-top:24px}
.featured{left:0;top:145px;width:1096px;height:337px;background:var(--band)}
.section-title{width:1096px;text-align:center;font-size:18px;font-weight:500;color:var(--ink);letter-spacing:.4px}
.pager{display:flex;gap:2px}
.pager span{width:40px;height:28px;background:var(--red);display:flex;align-items:center;justify-content:center}
.card{top:207px;width:180px;height:206px;background:var(--white);border:1px solid #cfcfcf}
.card .photo{position:absolute;left:14px;top:30px;width:152px;height:166px;border-radius:4px}
.tag{position:absolute;left:-4px;top:10px;width:162px;height:22px;background:var(--red);color:var(--white);font-size:11px;font-weight:600;padding:4px 0 0 18px;clip-path:polygon(0 0,100% 0,88% 100%,0 100%)}
.card-name{top:420px;width:180px;text-align:center;font-size:11.5px;color:var(--muted);letter-spacing:.3px}
.card-price{top:436px;width:180px;text-align:center;font-size:13px;font-weight:500;color:var(--ink)}
.brand{top:556px;width:133px;height:40px;text-align:center;font-size:17px;font-weight:500;white-space:nowrap;line-height:22px;border-bottom:2px solid #d9d9d9}
.brand.long{font-size:15px}
.dash{left:102px;top:634px;width:936px;border-top:1px dashed #8a8a8a}
.feature{top:672px;width:140px;text-align:center}
.feature svg{display:block;margin:0 auto}
.feature p{margin-top:14px;font-size:11px;line-height:15px;font-weight:500;letter-spacing:.4px;color:var(--ink)}
.newsletter{left:0;top:810px;width:1096px;height:42px;background:var(--red)}
.newsletter h3{position:absolute;left:105px;top:10px;font-size:16px;font-weight:500;font-style:italic;letter-spacing:3.3px;color:var(--white)}
.field{position:absolute;top:7px;height:28px;background:var(--white);border-radius:5px;font-size:11px;letter-spacing:1.5px;color:var(--ink);padding:7px 0 0 13px}
.send{position:absolute;left:978px;top:7px;width:60px;height:28px;background:#8a8a8a;border-radius:5px;display:flex;align-items:center;justify-content:center}
.footer{left:0;top:852px;width:1096px;height:307px;background:var(--footer)}
.col-head{top:38px;font-size:16px;font-weight:500;color:var(--white);letter-spacing:.3px}
.links{top:68px;list-style:none;font-size:12.5px;color:var(--white);letter-spacing:.3px}
.links li{height:29px}
.contact-row{left:370px;display:flex;align-items:center;gap:14px;font-size:12.5px;color:var(--white);letter-spacing:.3px}
.icon-circle{width:26px;height:26px;border-radius:50%;background:var(--white);display:flex;align-items:center;justify-content:center}
.social{left:570px;width:26px;height:26px;border-radius:50%;background:var(--white);display:flex;align-items:center;justify-content:center}
.map{left:739px;top:28px;width:300px;height:260px;background:linear-gradient(135deg,#ecebe6,#dfe7d2 50%,#e8e6df);border:1px solid #cfcfcf}
.wordmark{left:104px;top:254px;font-size:32px;font-weight:600;letter-spacing:2px;color:var(--white)}
.bottom-bar{left:0;top:1159px;width:1096px;height:41px;background:var(--footer-dark);color:var(--white);font-size:11px;font-weight:500}
.bottom-bar span{position:absolute;top:14px}
</style>
</head>
<body>

<section class="intro">
  <div class="abs intro-art" role="img" aria-label="Illustration of a service representative in a red circle"></div>
  <div class="abs intro-text">
    <p>chairs, walking and mobility equipment, pressure care and daily living aids to Aged and Disabled individuals, and also to the Healthcare Industry.</p>
    <p>At Tolvena, we commit to delivering quality products and a best price guarantee. We offer each customer the freedom to choose which equipment is right for their lifestyle.</p>
  </div>
</section>

<section class="abs featured"></section>
<h2 class="abs section-title" style="left:0;top:166px">Featured Products</h2>
<div class="abs pager" style="left:957px;top:166px">
  <span><svg width="12" height="16" viewBox="0 0 12 16"><path d="M9 2 3 8l6 6" fill="none" stroke="#fff" stroke-width="2.5"/></svg></span>
  <span><svg width="12" height="16" viewBox="0 0 12 16"><path d="M3 2l6 6-6 6" fill="none" stroke="#fff" stroke-width="2.5"/></svg></span>
</div>

<div class="abs card" style="left:106px"><div class="photo" role="img" aria-label="Photo of a folding wheelchair" style="background:linear-gradient(160deg,#f2f2f2,#bdbdbd)"></div><div class="tag">Sale</div></div>
<div class="abs card" style="left:357px"><div class="photo" role="img" aria-label="Photo of an electric mobility scooter" style="background:linear-gradient(160deg,#f0f0f0,#9a9a9a)"></div><div class="tag">Sale</div></div>
<div class="abs card" style="left:607px"><div class="photo" role="img" aria-label="Photo of a massage recliner chair" style="background:linear-gradient(160deg,#e9e9e9,#8e2a2f)"></div><div class="tag">Sale</div></div>
<div class="abs card" style="left:858px"><div class="photo" role="img" aria-label="Photo of a freestanding shower chair" style="background:linear-gradient(160deg,#f6f6f6,#cfcfcf)"></div><div class="tag">Sale</div></div>

<div class="abs card-name" style="left:106px">Transit Lite Wheel Chair</div>
<div class="abs card-price" style="left:106px">$219</div>
<div class="abs card-name" style="left:357px">Electric Scooter</div>
<div class="abs card-price" style="left:357px">$219</div>
<div class="abs card-name" style="left:607px">Massage Recliner</div>
<div class="abs card-price" style="left:607px">$219</div>
<div class="abs card-name" style="left:858px">Freestanding Shower Chair</div>
<div class="abs card-price" style="left:858px">$219</div>

<h2 class="abs section-title" style="left:0;top:504px">Our Brands</h2>
<div class="abs pager" style="left:957px;top:499px">
  <span><svg width="12" height="16" viewBox="0 0 12 16"><path d="M9 2 3 8l6 6" fill="none" stroke="#fff" stroke-width="2.5"/></svg></span>
  <span><svg width="12" height="16" viewBox="0 0 12 16"><path d="M3 2l6 6-6 6" fill="none" stroke="#fff" stroke-width="2.5"/></svg></span>
</div>
<div class="abs brand" style="left:102px;color:#5a6f8a">Airvale</div>
<div class="abs brand" style="left:263px;color:#c8321e">Hearthly</div>
<div class="abs brand" style="left:424px;color:#1d5f86">Kestral</div>
<div class="abs brand" style="left:584px;color:#c4161c">Liftora</div>
<div class="abs brand long" style="left:745px;color:#34425a">Pemberly Medical</div>
<div class="abs brand" style="left:905px;color:#1f3f7a">Summitra</div>

<div class="abs dash"></div>

<div class="abs feature" style="left:59px">
  <svg width="56" height="70" viewBox="0 0 56 70"><path d="M14 40 4 62l10-3 5 9 9-24M42 40l10 22-10-3-5 9-9-24" fill="#7a7a7a"/><circle cx="28" cy="24" r="22" fill="#7a7a7a"/><circle cx="28" cy="24" r="16" fill="none" stroke="#fff" stroke-width="2"/><path d="M25 16l5-3v22" stroke="#fff" stroke-width="3" fill="none"/></svg>
  <p>NO 1<br>SUPPLIER</p>
</div>
<div class="abs feature" style="left:284px">
  <svg width="68" height="70" viewBox="0 0 68 70"><circle cx="34" cy="34" r="33" fill="#7a7a7a"/><circle cx="34" cy="34" r="22" fill="#fff"/></svg>
  <p>ISO 9001<br>SUPPLIER</p>
</div>
<div class="abs feature" style="left:499px">
  <svg width="60" height="70" viewBox="0 0 60 70"><g fill="none" stroke="#7a7a7a" stroke-width="3"><rect x="14" y="4" width="26" height="22"/><rect x="14" y="28" width="26" height="22"/><rect x="14" y="52" width="26" height="12"/><rect x="42" y="28" width="14" height="36"/><path d="M4 10v56h52"/></g><circle cx="8" cy="66" r="3" fill="#7a7a7a"/><circle cx="54" cy="66" r="3" fill="#7a7a7a"/></svg>
  <p>HUGE RANGE OF<br>PRODUCTS</p>
</div>
<div class="abs feature" style="left:715px">
  <svg width="60" height="70" viewBox="0 0 60 70"><g fill="none" stroke="#7a7a7a" stroke-width="3"><circle cx="12" cy="36" r="8"/><circle cx="46" cy="12" r="8"/><circle cx="46" cy="60" r="8"/><path d="M19 32 39 16M19 40l20 16"/></g></svg>
  <p>VAST SUPPLY<br>PRODUCTS</p>
</div>
<div class="abs feature" style="left:936px">
  <svg width="64" height="70" viewBox="0 0 64 70"><path d="M10 36a22 22 0 0 1 44 0" fill="none" stroke="#7a7a7a" stroke-width="5"/><rect x="4" y="30" width="10" height="18" rx="4" fill="#7a7a7a"/><rect x="50" y="30" width="10" height="18" rx="4" fill="#7a7a7a"/><path d="M54 48q0 12-16 12" fill="none" stroke="#7a7a7a" stroke-width="3"/><path d="M10 70q0-14 22-14t22 14z" fill="#7a7a7a"/></svg>
  <p>FRIENDLY<br>Cusomer Care</p>
</div>

<section class="abs newsletter">
  <h3>Newsletter Sign Up Stay Up to Date with News and Events</h3>
  <div class="field" style="left:761px;width:96px">Your Name</div>
  <div class="field" style="left:869px;width:96px">Your Email</div>
  <div class="send"><svg width="18" height="16" viewBox="0 0 18 16"><path d="M1 8 17 1 13 15 9 10 16 3 7 9z" fill="#fff"/></svg></div>
</section>

<footer class="abs footer">
  <h4 class="abs col-head" style="left:106px">Menu</h4>
  <ul class="abs links" style="left:108px"><li>Home</li><li>Products</li><li>Services</li><li>About Us</li><li>Contact</li></ul>

  <h4 class="abs col-head" style="left:214px">Our Products</h4>
  <ul class="abs links" style="left:215px"><li>Massage Products</li><li>Walking Aids</li><li>Electric Scooter</li><li>Daily Aids</li><li>Consumer Health</li><li>Wound Care</li></ul>

  <h4 class="abs col-head" style="left:370px">Contact</h4>
  <div class="abs contact-row" style="top:64px"><span class="icon-circle"><svg width="14" height="14" viewBox="0 0 14 14"><path d="M3 1l2 3-1 2q1 3 4 4l2-1 3 2-1 2Q6 13 1 3z" fill="#737373"/></svg></span>68 410 357</div>
  <div class="abs contact-row" style="top:109px"><span class="icon-circle"><svg width="14" height="12" viewBox="0 0 14 12"><rect x="1" y="2" width="12" height="9" fill="#737373"/><path d="M1 2l6 5 6-5" fill="none" stroke="#fff" stroke-width="1.2"/></svg></span>info@tolvenacare.com</div>
  <div class="abs contact-row" style="top:151px"><span class="icon-circle"><svg width="14" height="14" viewBox="0 0 14 14"><rect x="4" y="1" width="6" height="4" fill="#737373"/><rect x="1" y="5" width="12" height="6" rx="1" fill="#737373"/><rect x="4" y="9" width="6" height="4" fill="#fff" stroke="#737373"/></svg></span>68 410 357</div>
  <div class="abs contact-row" style="top:196px"><span class="icon-circle"><svg width="12" height="16" viewBox="0 0 12 16"><path d="M6 1a5 5 0 0 1 5 5c0 4-5 9-5 9S1 10 1 6a5 5 0 0 1 5-5z" fill="#737373"/><circle cx="6" cy="6" r="2" fill="#fff"/></svg></span>12 Ridgeway St, Parkvale</div>

  <h4 class="abs col-head" style="left:570px">Keep Connected</h4>
  <div class="abs social" style="top:64px" aria-label="Share">
    <svg width="14" height="14" viewBox="0 0 14 14"><g fill="#737373"><circle cx="3" cy="7" r="2"/><circle cx="11" cy="3" r="2"/><circle cx="11" cy="11" r="2"/></g><path d="M3 7l8-4M3 7l8 4" stroke="#737373" stroke-width="1.3"/></svg>
  </div>
  <div class="abs social" style="top:109px" aria-label="Message">
    <svg width="14" height="14" viewBox="0 0 14 14"><path d="M1 2h12v8H6l-3 3v-3H1z" fill="#737373"/></svg>
  </div>
  <div class="abs social" style="top:153px" aria-label="Website">
    <svg width="14" height="14" viewBox="0 0 14 14"><g fill="none" stroke="#737373" stroke-width="1.3"><circle cx="7" cy="7" r="5.5"/><ellipse cx="7" cy="7" rx="2.3" ry="5.5"/><path d="M1.5 7h11"/></g></svg>
  </div>

  <div class="abs map" role="img" aria-label="Street map showing the store location"></div>

  <div class="abs wordmark">TOLVENA</div>
</footer>

<div class="abs bottom-bar">
  <span style="left:104px">Copyright © 2017 Tolvena Mobility</span>
  <span style="left:681px">Copyright Information</span>
  <span style="left:830px">Terms and Condition</span>
  <span style="left:970px">Privacy Policy</span>
</div>

</body>
</html>
```